Packaged Food Business Needs a Packaging Design

We need a package design to be used as a label/sticker on the lids of round and square transparent plastic containers and on the sides of resealable stand-up pouches. The brand name is 'Tastora' - please find attached logo together with pictures of the sample containers and pouch. We will use the packaging to market a wide variety of food categories from nuts, dried fruits, spices, cooking chocolates, baking ingredients, cereals, grains and pulses.

OVERALL FEEDBACK ON DESIGNS ALREADY RECEIVED:

- We have found so far that a lot of our mandatory requirements are not adhered to in designs that have been submitted so far. We would like to emphasise that the ingredient, weight and expiry text will be printed at the time of packing so it should not take prime space on the pack BUT at the same time some 'blank' space needs to flawlessly be incorporated into the overall design for this purpose
- We encourage you to glorify the brand logo in the pack, and absolutely refrain from duplicating the tagline
- Please note that ONE label design will be used to pack a wide variety of food ingredients and therefore please ensure that the choice of your design incorporates this requirement, in the past we have received designs that are limited to only one type of food (like nuts) or have received designs that are too floral or leafy (and not grounded to food
- Please ensure that you submit designs for all three packaging formats, it is critical to see the family look from the on-set

Target Market(s)

The brand is targeting both mothers and professional chefs and therefore the label design should be broadly approachable and convey affordable premium

Industry/Entity Type

Business

Requirements
Must have
• - Consistent with the brand name and logo, the overall look and feel of the packaging should convey values of healthy, gourmet food ingredients, high in nourishment and project a sense of delightful taste
• - The design styling to be modern and 'simplistic' (embracing 'less-is-more' type of a design style)
• - Design a packaging architecture that incorporates the brand logo together with its tagline lock-up of 'savour the goodness in every morsel' - find logo attached
• - The design needs to have a dedicated area to print the ingredient (e.g., Mixed Nuts), weight (e.g., 500g) and expiry (this space needs to be flawlessly incorporated into the design) - this information will be printed either with an inkjet printer or with a rubber stamp so please leave an empty space (the text should not be part of the design, just the area for the text needs to be included in the design)
• - The packaging must include 'Packed By: Kelvane Distributors Ltd, P. O. Box 51946, Kampala - Uganda'
• - For the design of the resealable pouch, please incorporate a window to see through the ingredients and a hole on top to hang on supermarket pegs if necessary
Nice to have
• - We would love to have some design submissions that are bold and cheerful and fun (but not frivolous) - please see attached inspiration for 'fun' packaging. The attachments are purely for inspiration, not to infringe on anyone else's TM and copyrights
• - Incorporate green to convey healthy, organic values
• - Explore use of gold and silver convey premiumness
Should not have
• - Do not duplicate the tagline
• - Do not include the ingredient, weight and expiry in the main graphic of the design, these will be printed at the time of packing so ensure there is provision for this in a flawless way in the design (e.g., via a blank space allocated for this purpose)

```html
<!DOCTYPE html>
<html lang="en">
<head>
<meta charset="utf-8">
<title>Tastora – Lid &amp; Pouch Label</title>
<link href="https://fonts.googleapis.com/css2?family=Roboto+Slab:wght@800&family=Montserrat:wght@500;700&display=swap" rel="stylesheet">
<style>
  :root {
    --page-bg: #f3f3f3;
    --silver-light: #dcdfe1;
    --silver-mid: #b8bdc0;
    --silver-dark: #979ca0;
    --cartouche-fill: #ffffff;
    --cartouche-edge: #8fb3a8;
    --brand-brown: #5a3a22;
    --brand-green: #6a9a2f;
    --legal-ink: #2f3133;
  }
  html, body {
    margin: 0;
    padding: 0;
    width: 1200px;
    height: 1000px;
    overflow: hidden;
    background: var(--page-bg);
  }
  .label-canvas {
    display: block;
    width: 1200px;
    height: 1000px;
  }
  .brand-name {
    font-family: "Roboto Slab", Georgia, serif;
    font-weight: 800;
    font-size: 70px;
    letter-spacing: 6px;
    fill: var(--brand-brown);
  }
  .brand-tagline {
    font-family: "Montserrat", Arial, sans-serif;
    font-weight: 700;
    font-size: 15px;
    letter-spacing: 1.5px;
    fill: var(--brand-green);
    text-transform: uppercase;
  }
  .packer-line {
    font-family: "Montserrat", Arial, sans-serif;
    font-weight: 500;
    font-size: 21px;
    fill: var(--legal-ink);
  }
</style>
</head>
<body>
<svg class="label-canvas" viewBox="0 0 1200 1000" xmlns="http://www.w3.org/2000/svg">
  <defs>
    <linearGradient id="silverFoil" x1="0" y1="0" x2="1" y2="1">
      <stop offset="0" stop-color="var(--silver-mid)"/>
      <stop offset="0.45" stop-color="var(--silver-light)"/>
      <stop offset="0.7" stop-color="var(--silver-mid)"/>
      <stop offset="1" stop-color="var(--silver-dark)"/>
    </linearGradient>
    <path id="packerArc" d="M 225 500 A 375 375 0 0 0 975 500"/>
  </defs>

  <g class="round-label">
    <circle class="label-disc" cx="600" cy="500" r="420" fill="url(#silverFoil)"
            role="img" aria-label="Brushed silver background with a faint geometric star pattern"/>

    <path class="print-cartouche"
          d="M 400 380 Q 600 345 800 380 A 30 30 0 0 0 830 410 L 830 590 A 30 30 0 0 0 800 620 Q 600 655 400 620 A 30 30 0 0 0 370 590 L 370 410 A 30 30 0 0 0 400 380 Z"
          fill="var(--cartouche-fill)" stroke="var(--cartouche-edge)" stroke-width="5"/>

    <g class="brand-lockup">
      <circle class="brand-dot" cx="600" cy="392" r="11" fill="var(--brand-green)"/>
      <text class="brand-name" x="600" y="462" text-anchor="middle">TASTORA</text>
      <text class="brand-tagline" x="600" y="488" text-anchor="middle">savour the goodness in every morsel</text>
    </g>

    <text class="packer-line">
      <textPath href="#packerArc" startOffset="50%" text-anchor="middle">Packed by Kelvane Distributors Ltd&#160;&#160;P. O. Box 51946, Kampala - Uganda</textPath>
    </text>
  </g>
</svg>
</body>
</html>
```